Accounting Practice Business Card Design

I have a logo I am happy for you to use in the design of the Business Card.
You can edit and change colours as you please, I am not fixated on it.
I am looking for a modern and clean overall feel for the finished design.

The business is a small accounting practice who thrives on word of mouth referrals and this card will be given to all current and prospect clients.

Industry/Entity Type

Accountant

Contact Information for Business Card

Marcus Elwin
Level 5, 8 Corvale Ridge Road
ASHGROVE RISE VIC 3187
Phone: 9481 3057
Email: melwin@mrfaccountants.com.au
Web: www.mrfaccountants.com.au

Font styles to use
Serif
Sans Serif

Colors
0555a3
3277b5
85acd3
0393ce
33a6d7
85cae6
00a990
33b8a4
9bcb3c

Requirements
Must have
• "The end to your tax problems begin with us"
• "A referral from you is our greatest compliment"
Nice to have
• Modern clean professional

```html
<!DOCTYPE html>
<html lang="en">
<head>
<meta charset="utf-8">
<title>MRF Accountants – Business Card</title>
<link href="https://fonts.googleapis.com/css2?family=Arimo:wght@400;700&display=swap" rel="stylesheet">
<style>
  :root {
    --backdrop: #2a2a2a;
    --card-white: #ffffff;
    --brand-navy: #0e3b78;
    --brand-blue: #12457a;
    --text-grey: #5a5a5a;
    --text-white: #ffffff;
  }
  * { margin: 0; padding: 0; box-sizing: border-box; }
  html, body {
    width: 1200px;
    height: 960px;
    overflow: hidden;
    background: var(--backdrop);
    font-family: "Arimo", Arial, sans-serif;
  }
  .canvas {
    position: relative;
    width: 1200px;
    height: 960px;
  }
  .card {
    position: absolute;
    top: 193px;
    width: 328px;
    height: 574px;
  }
  .card-front {
    left: 236px;
    background: var(--card-white);
  }
  .card-back {
    left: 605px;
    background: var(--brand-blue);
  }
  .person-name {
    position: absolute;
    left: 42px;
    top: 44px;
    font-size: 20px;
    font-weight: 700;
    color: var(--brand-navy);
  }
  .person-role {
    position: absolute;
    left: 42px;
    top: 69px;
    font-size: 16px;
    color: var(--text-grey);
  }
  .address {
    position: absolute;
    left: 42px;
    top: 121px;
    font-size: 13.5px;
    line-height: 19.5px;
    color: var(--text-grey);
    font-style: normal;
  }
  .contact-list {
    position: absolute;
    left: 42px;
    top: 167px;
    list-style: none;
    font-size: 13.5px;
    line-height: 19.5px;
    color: var(--text-grey);
  }
  .contact-list li {
    display: flex;
    align-items: center;
    gap: 6px;
  }
  .contact-icon {
    width: 10px;
    height: 10px;
    fill: var(--brand-navy);
    flex: none;
  }
  .brand-name-front {
    position: absolute;
    right: 36px;
    top: 462px;
    font-size: 22px;
    font-weight: 700;
    color: var(--brand-navy);
    letter-spacing: 0.5px;
  }
  .tagline-front {
    position: absolute;
    left: 0;
    right: 0;
    top: 517px;
    text-align: center;
    font-size: 12.5px;
    color: var(--text-grey);
  }
  .brand-name-back {
    position: absolute;
    left: 37px;
    top: 46px;
    font-size: 24px;
    font-weight: 700;
    color: var(--text-white);
    letter-spacing: 0.5px;
  }
  .referral-quote {
    position: absolute;
    left: 37px;
    top: 484px;
    font-size: 15.5px;
    line-height: 23px;
    color: var(--text-white);
  }
  .referral-quote strong {
    font-size: 21px;
    font-weight: 700;
  }
  .referral-quote .emph {
    font-size: 19px;
    font-weight: 700;
  }
</style>
</head>
<body>
<main class="canvas">
  <section class="card card-front" aria-label="Business card front">
    <h1 class="person-name">Marcus Elwin</h1>
    <p class="person-role">Accountant</p>
    <address class="address">
      Level 5, 8 Corvale Ridge Road<br>
      ASHGROVE RISE VIC 3187
    </address>
    <ul class="contact-list">
      <li>
        <svg class="contact-icon" viewBox="0 0 10 10" aria-hidden="true"><path d="M2 1 L3.5 0.5 L4.5 2.5 L3.4 3.3 Q4.2 5.6 6.6 6.6 L7.5 5.5 L9.5 6.5 L9 8 Q5 9.5 1.5 5.5 Q0.5 3 2 1 Z"/></svg>
        <span>9481 3057</span>
      </li>
      <li>
        <svg class="contact-icon" viewBox="0 0 10 10" aria-hidden="true"><path d="M0 2 H10 V8 H0 Z M0.8 2.6 L5 5.6 L9.2 2.6" stroke="#fff" stroke-width="0.8"/></svg>
        <span>melwin@mrfaccountants.com.au</span>
      </li>
      <li>
        <svg class="contact-icon" viewBox="0 0 10 10" aria-hidden="true"><circle cx="5" cy="5" r="4.6"/><path d="M0.5 5 H9.5 M5 0.5 V9.5 M5 0.5 Q2.5 5 5 9.5 M5 0.5 Q7.5 5 5 9.5" stroke="#fff" stroke-width="0.6" fill="none"/></svg>
        <span>www.mrfaccountants.com.au</span>
      </li>
    </ul>
    <p class="brand-name-front">MRF ACCOUNTANTS</p>
    <p class="tagline-front">"The end to your tax problems begin with us"</p>
  </section>

  <section class="card card-back" aria-label="Business card back">
    <p class="brand-name-back">MRF ACCOUNTANTS</p>
    <p class="referral-quote">"A <strong>referral</strong> from<br>you is our greatest <span class="emph">compliment</span>"</p>
  </section>
</main>
</body>
</html>
```